Business Card Design

Business Card for professional consulting firm working with large financial institutions.

Target Market(s)

Executive buyers

Industry/Entity Type

Banking

Contact Information for Business Card

Mild creativity wanted. Not boring, but do elaborate artwork.

Font styles to use
Serif
Sans Serif

Colors

Designer to choose colors to be used in the design.

Requirements
Must have
• Standard business card features - company name, individual name, telephone, website, email, locations.
Nice to have
• Two colors
Should not have
• too many colors, fancy printing, cartoons.

```html
<!DOCTYPE html>
<html lang="en">
<head>
<meta charset="utf-8">
<title>Corvantis Business Card</title>
<link rel="stylesheet" href="https://fonts.googleapis.com/css2?family=Source+Serif+4:opsz,wght@8..60,400;8..60,600;8..60,700&display=swap">
<style>
  :root {
    --navy: #262262;
    --navy-soft: #3a3678;
    --white: #ffffff;
    --page: #ffffff;
    --ink: #1c1c2a;
    --grey: #6d6d74;
    --mist: #f1f1f3;
    --serif: "Source Serif 4", Georgia, serif;
  }
  * { margin: 0; padding: 0; box-sizing: border-box; }
  html, body { width: 1000px; height: 1200px; overflow: hidden; }
  body { position: relative; background: var(--page); font-family: var(--serif); }

  .card { position: absolute; left: 175px; width: 698px; height: 419px; overflow: hidden; }
  .card--front { top: 75px; background: var(--white); }
  .card--back { top: 663px; background: var(--white); }

  /* front */
  .front__field {
    position: absolute; left: 0; top: 0; width: 100%; height: 335px;
    background: radial-gradient(ellipse at 50% 45%, var(--navy-soft) 0%, var(--navy) 70%);
  }
  .front__brand {
    position: absolute; left: 0; top: 132px; width: 100%; text-align: center;
    color: var(--white); font-size: 46px; font-weight: 400; letter-spacing: 0.5px; line-height: 1;
  }
  .front__web {
    position: absolute; left: 0; top: 364px; width: 100%; text-align: center;
    color: var(--navy); font-size: 20px; letter-spacing: 1px; line-height: 1;
  }
  .front__web b { font-weight: 700; }

  /* back */
  .back__field {
    position: absolute; left: 180px; top: 10px; width: 518px; height: 205px;
    background: radial-gradient(ellipse at 60% 55%, var(--mist) 0%, var(--white) 70%);
  }
  .back__address {
    position: absolute; left: 51px; top: 80px; color: var(--ink);
    font-size: 20px; font-weight: 600; line-height: 29px;
  }
  .back__rule { position: absolute; left: 46px; top: 153px; width: 309px; height: 6px; background: var(--navy); }
  .back__brand {
    position: absolute; left: 440px; top: 105px; color: var(--grey);
    font-size: 21px; font-weight: 400; line-height: 1;
  }
  .back__band { position: absolute; left: 0; top: 220px; width: 100%; height: 199px; background: var(--navy); }
  .person { position: absolute; left: 73px; top: 280px; color: var(--white); }
  .person__name { font-size: 31px; font-weight: 400; line-height: 1; letter-spacing: 0.3px; }
  .person__name b { font-weight: 700; }
  .person__role { font-size: 19px; margin-top: 6px; line-height: 1; }
  .back__divider { position: absolute; left: 294px; top: 262px; width: 2px; height: 97px; background: var(--white); }
  .contact { position: absolute; left: 320px; top: 268px; list-style: none; color: var(--white); }
  .contact__item { display: flex; align-items: center; height: 28px; font-size: 19px; }
  .contact__icon { width: 20px; height: 20px; margin-right: 14px; flex: none; }
</style>
</head>
<body>
  <section class="card card--front">
    <div class="front__field" role="img" aria-label="Soft swirling ring pattern on navy"></div>
    <div class="front__brand">corvantis</div>
    <div class="front__web">www.<b>corvantis</b>.com</div>
  </section>

  <section class="card card--back">
    <div class="back__field" role="img" aria-label="Faint grey swirling ring pattern"></div>
    <p class="back__address">42 Meridian Ave. Halden,<br>PA 3190, United Kingdom</p>
    <div class="back__rule"></div>
    <div class="back__brand">corvantis</div>

    <div class="back__band"></div>
    <div class="person">
      <p class="person__name"><b>JOHN</b> DOE</p>
      <p class="person__role">Founder &amp; CEO</p>
    </div>
    <div class="back__divider"></div>
    <ul class="contact">
      <li class="contact__item">
        <svg class="contact__icon" viewBox="0 0 20 20" aria-hidden="true">
          <circle cx="10" cy="10" r="10" fill="#fff"/>
          <rect x="7" y="4.5" width="6" height="11" rx="1.2" fill="#262262"/>
          <rect x="8" y="6" width="4" height="6" fill="#fff"/>
        </svg>555 - 555 - 555
      </li>
      <li class="contact__item">
        <svg class="contact__icon" viewBox="0 0 20 20" aria-hidden="true">
          <circle cx="10" cy="10" r="10" fill="#fff"/>
          <rect x="5" y="6.5" width="10" height="7" fill="none" stroke="#262262" stroke-width="1.4"/>
          <path d="M5 6.5 L10 10.5 L15 6.5" fill="none" stroke="#262262" stroke-width="1.4"/>
        </svg>johnd@corvantis.com
      </li>
      <li class="contact__item">
        <svg class="contact__icon" viewBox="0 0 20 20" aria-hidden="true">
          <circle cx="10" cy="10" r="10" fill="#fff"/>
          <circle cx="10" cy="10" r="5.5" fill="none" stroke="#262262" stroke-width="1.3"/>
          <ellipse cx="10" cy="10" rx="2.4" ry="5.5" fill="none" stroke="#262262" stroke-width="1.2"/>
          <line x1="4.5" y1="10" x2="15.5" y2="10" stroke="#262262" stroke-width="1.2"/>
        </svg>www.corvantis.com
      </li>
    </ul>
  </section>
</body>
</html>
```